Rollvane Supply .com

This website is simple!!!
Landing page background image should capture the customers attention!!! We will provide a image as a example of what we like. The purpose for this website is to provide customers with a clean easy way to request a quote for industrial casters and wheels by OEM’s as well as maintenance departments worldwide. Please see if you can follow our thought process below.
Customer comes to website, they are invited to Request a Quote by providing us with Manufacturer Name, Manufacturers Part # and quantity needed.
If this is not known the customer will complete will WP conversation format form answering about 10 questions
Or
Look up the part number in one of the 8 to 12 catalogs located in the Pagewhirl Deck format on our catalog page, or equal plug in .
When the client request a quote a account page will pop up request The following:
Clients first and last name
Email address
And optional questions
Company name and best contact number.
Once this is complete customer will hit SUBMIT.
The customers request will be in system. A email will be sent to Customer service notifying us the Quote Request has been made.
We will then build a quote for the customer with a good, better and best options. Customers Request a Quote submission may have more than one caster or wheel requested at a time, so website must allow this.
When the customer comes back into website there email address will come up as the account name and request a password be made for them. This will allow them to store quotes in their account for future needs. If quote is older than 30 day the system will trigger a button at the bottom of the quote for resubmit Request for updated quote.
Once customer reviews quote the quote can be Converted to order within the website.
Once Converted the system will send us a email and order will be processed.
We will need a Chat program that will text to CS the questions.
You will need to have high quality graphic design skills on your team.
We have found 2 plugins that would work nicely with our new website Pagewhirl decks to showcase our catalogs for customers to research and QuillKit conversation forms to complete request for quote form.
Just Ideas:
Very very ghosted caster blueprint in white background but very very ghosted or the icon just idea
We have never had a font used we like
Grayscale every except for rubber on wheels and logo icon
Website should have hamburger menu on left
Website should hav responsive deign
Account head on right side
Has anyone read the brief from top to bottom and the updates, I’m seeing a lot of duplicates of the website I posted in images I want a clean website With lite backgrand with the poly being definite colors on each wheel I added a green yellow and red image has anyone looked at that Just a question?
Went on vacation/holiday

```html
<!DOCTYPE html>
<html lang="en">
<head>
<meta charset="utf-8">
<title>Rollvane Supply .com — Contact Form</title>
<link rel="stylesheet" href="https://fonts.googleapis.com/css2?family=Exo+2:wght@500;600;700&family=Open+Sans:wght@400;600;700&display=swap">
<style>
  :root {
    --bg-top: #1a5cae;
    --bg-mid: #2448a8;
    --bg-bottom: #3a2c9c;
    --white: #ffffff;
    --field-bg: #e9e9ea;
    --field-border: #c9c9cc;
    --field-focus: #29a8e8;
    --placeholder: #8a8a8e;
    --title: #243f8f;
    --note: #6f6f74;
    --submit-a: #0f9af0;
    --submit-b: #3cbcff;
    --ghost-field: rgba(255,255,255,0.22);
    --ghost-text: rgba(255,255,255,0.55);
    --caster-grey: #9aa3b3;
    --caster-rubber: #1e3f8a;
  }
  * { box-sizing: border-box; margin: 0; padding: 0; }
  html, body { width: 1200px; height: 524px; overflow: hidden; }
  body { font-family: "Open Sans", sans-serif; }

  .canvas {
    position: relative; width: 1200px; height: 524px; overflow: hidden;
    background: linear-gradient(160deg, var(--bg-top) 0%, var(--bg-mid) 55%, var(--bg-bottom) 100%);
  }

  /* blurred landing page behind the modal */
  .landing { position: absolute; inset: 0; filter: blur(3px); color: var(--white); }
  .landing__shape {
    position: absolute; background: rgba(255,255,255,0.06); transform: rotate(45deg);
  }
  .brand {
    position: absolute; left: 225px; top: 30px; display: flex; align-items: center; gap: 8px;
    font-family: "Exo 2", sans-serif; font-weight: 700; font-size: 21px; color: rgba(255,255,255,0.85);
  }
  .brand__mark { width: 26px; height: 26px; border: 3px solid rgba(255,255,255,0.85); border-radius: 50%; }
  .nav { position: absolute; left: 565px; top: 38px; display: flex; gap: 34px;
    font-family: "Exo 2", sans-serif; font-weight: 700; font-size: 8px; color: var(--ghost-text); }
  .nav__item--active { border-bottom: 2px solid var(--ghost-text); }
  .account { position: absolute; left: 888px; top: 30px; width: 24px; height: 24px;
    border: 2px solid var(--ghost-text); border-radius: 50%; }
  .login { position: absolute; left: 926px; top: 28px; width: 50px; height: 28px;
    border: 2px solid var(--ghost-text); border-radius: 3px;
    font-family: "Exo 2", sans-serif; font-weight: 700; font-size: 8px; color: var(--ghost-text);
    display: flex; align-items: center; justify-content: center; }

  .hero__title { position: absolute; left: 223px; top: 140px;
    font-family: "Exo 2", sans-serif; font-weight: 700; font-size: 31px; color: rgba(255,255,255,0.85); }
  .steps { position: absolute; left: 225px; top: 197px; list-style: none; font-size: 12px; color: var(--ghost-text); }
  .steps li { height: 19.5px; }
  .steps b { display: inline-block; width: 18px; }
  .ghost-field { position: absolute; left: 225px; width: 150px; height: 26px; background: var(--ghost-field);
    border-radius: 2px; font-size: 9px; color: var(--ghost-text); padding: 7px 10px; }
  .ghost-btn { position: absolute; top: 386px; height: 33px; border-radius: 3px;
    font-family: "Exo 2", sans-serif; font-weight: 700; font-size: 9px; display: flex; align-items: center; justify-content: center; }
  .ghost-btn--quote { left: 226px; width: 111px; background: rgba(255,255,255,0.35); color: rgba(255,255,255,0.6); }
  .ghost-btn--alt { left: 345px; width: 60px; background: #1a8fe0; }
  .hero__note { position: absolute; left: 225px; top: 444px; width: 220px; font-size: 8px; line-height: 10.5px; color: var(--ghost-text); }

  .caster-photo { position: absolute; left: 800px; top: 110px; width: 140px; height: 320px;
    border-radius: 20px 60px 60px 20px;
    background: radial-gradient(circle at 40% 35%, #c7ccd6 0%, var(--caster-grey) 35%, var(--caster-rubber) 75%, transparent 100%); }

  /* modal */
  .modal { position: absolute; left: 373px; top: 80px; width: 454px; height: 392px;
    background: var(--white); border-radius: 3px; box-shadow: 0 6px 28px rgba(10,20,60,0.35); }
  .modal__close { position: absolute; left: 429px; top: 8px; }
  .modal__title { position: absolute; left: 0; right: 0; top: 19px; text-align: center;
    font-family: "Exo 2", sans-serif; font-weight: 500; font-size: 17px; color: var(--title); letter-spacing: 0.3px; }
  .field { position: absolute; left: 117px; width: 220px; height: 26px;
    background: var(--field-bg); border: 1px solid var(--field-border); border-radius: 3px;
    font: 400 9px "Open Sans", sans-serif; color: var(--placeholder); padding: 0 10px; line-height: 24px; }
  .field--focus { border-color: var(--field-focus); background: #ebeff1; }
  .field--area { height: 64px; line-height: 1; padding-top: 9px; }
  .modal__note { position: absolute; left: 127px; top: 318px; font-size: 8px; font-weight: 700; color: var(--note); }
  .submit { position: absolute; left: 177px; top: 338px; width: 100px; height: 34px; border-radius: 3px;
    background: linear-gradient(90deg, var(--submit-a) 0%, var(--submit-a) 70%, var(--submit-b) 100%);
    color: var(--white); font: 700 10px "Open Sans", sans-serif; letter-spacing: 0.3px;
    display: flex; align-items: center; justify-content: center; }
</style>
</head>
<body>
<main class="canvas">
  <div class="landing" aria-hidden="true">
    <div class="landing__shape" style="left:60px;top:-80px;width:220px;height:220px;"></div>
    <div class="landing__shape" style="left:980px;top:90px;width:200px;height:200px;"></div>
    <div class="landing__shape" style="left:930px;top:260px;width:180px;height:180px;"></div>

    <div class="brand"><span class="brand__mark"></span>Rollvane Supply .com</div>
    <nav class="nav">
      <span class="nav__item nav__item--active">ABOUT US</span>
      <span class="nav__item">OUR CATALOG</span>
      <span class="nav__item">CONTACTS</span>
    </nav>
    <span class="account"></span>
    <span class="login">LOGIN</span>

    <h1 class="hero__title">Easy as 1-2-3</h1>
    <ol class="steps">
      <li><b>1</b>Request a Quote</li>
      <li><b>2</b>Receive a Quote</li>
      <li><b>3</b>Convert to Quote or Order</li>
    </ol>
    <div class="ghost-field" style="top:267px;">Manufacturer Name</div>
    <div class="ghost-field" style="top:306px;">Manufacturers Part #</div>
    <div class="ghost-field" style="top:345px;">Quantity</div>
    <div class="ghost-btn ghost-btn--quote">REQUEST A QUOTE</div>
    <div class="ghost-btn ghost-btn--alt"></div>
    <p class="hero__note">Look up the part number in one of our catalogs in the Pagewhirl Deck format on our catalog page</p>

    <div class="caster-photo" role="img" aria-label="Photo of an industrial swivel caster with a blue rubber wheel"></div>
  </div>

  <section class="modal" aria-label="Contact Form">
    <svg class="modal__close" width="17" height="17" viewBox="0 0 17 17" aria-label="Close">
      <circle cx="8.5" cy="8.5" r="7.5" fill="none" stroke="#8b8b90" stroke-width="1.2"/>
      <path d="M5.5 5.5 L11.5 11.5 M11.5 5.5 L5.5 11.5" stroke="#8b8b90" stroke-width="1.2"/>
    </svg>
    <h2 class="modal__title">Contact Form</h2>
    <div class="field field--focus" style="top:52px;">First name*</div>
    <div class="field" style="top:91px;">Last name*</div>
    <div class="field" style="top:130px;">Email*</div>
    <div class="field field--area" style="top:169px;">Optional questions</div>
    <div class="field" style="top:246px;">Company name</div>
    <div class="field" style="top:285px;">Contact number*</div>
    <p class="modal__note">* - Required to fill</p>
    <div class="submit">SUBMIT</div>
  </section>
</main>
</body>
</html>
```